Ferncrest Dental, LLC business card project

Business card to be designed with current logo.
Dental office- please keep design of card that looks clean and professional.
Please include the following info:
Ferncrest Dental, LLC
Dr. Lorna Pettigrew
2871 Marlowe Street
Bethlehem, PA 18093
610-555-0193
ferncrestdental.office@examplemail.test
Hello everyone-
Reason: Just got back from overseas- will look at all designs and provide feedback. Thank you!
Reason: Polling my friends for the final selection-
thank you to all those that participated- so many talented designers!

```html
<!DOCTYPE html>
<html lang="en">
<head>
<meta charset="utf-8">
<title>Ferncrest Dental — Business Card</title>
<link href="https://fonts.googleapis.com/css2?family=Open+Sans:wght@400;600;700&display=swap" rel="stylesheet">
<style>
  :root {
    --backdrop: #1c1c1c;
    --card-white: #ffffff;
    --leaf-green: #5e9e34;
    --band-green: #58963a;
    --band-green-deep: #4a8430;
    --lime: #a9cf3a;
    --ink-light: #ffffff;
    --brand-green: #5fa236;
  }
  * { margin: 0; padding: 0; box-sizing: border-box; }
  html, body {
    width: 1200px;
    height: 806px;
    overflow: hidden;
    background: var(--backdrop);
    font-family: "Open Sans", Arial, sans-serif;
  }
  .stage {
    position: relative;
    width: 1200px;
    height: 806px;
    display: flex;
    align-items: center;
    justify-content: center;
  }
  .business-card {
    position: relative;
    width: 1000px;
    height: 571px;
    border-radius: 48px;
    overflow: hidden;
    background: var(--card-white);
  }
  .card-art {
    position: absolute;
    inset: 0;
    width: 100%;
    height: 100%;
  }
  .brand {
    position: absolute;
    left: 70px;
    top: 150px;
    display: flex;
    align-items: center;
    gap: 22px;
  }
  .brand-dot {
    width: 56px;
    height: 56px;
    border-radius: 50%;
    background: var(--brand-green);
  }
  .brand-name {
    font-weight: 400;
    font-size: 66px;
    letter-spacing: -1px;
    color: var(--brand-green);
    line-height: 1;
  }
  .doctor-name {
    position: absolute;
    right: 60px;
    top: 70px;
    font-weight: 600;
    font-size: 30px;
    color: var(--leaf-green);
  }
  .contact {
    position: absolute;
    color: var(--ink-light);
    font-weight: 700;
    font-size: 23px;
    line-height: 1.45;
  }
  .contact-phone {
    left: 60px;
    top: 400px;
    width: 470px;
    text-align: right;
  }
  .contact-email {
    left: 60px;
    top: 438px;
  }
  .contact-address {
    left: 575px;
    top: 470px;
    font-size: 24px;
  }
</style>
</head>
<body>
<main class="stage">
  <section class="business-card" aria-label="Ferncrest Dental business card">
    <svg class="card-art" viewBox="0 0 1000 571" preserveAspectRatio="none" aria-hidden="true">
      <defs>
        <linearGradient id="bandFill" x1="0" y1="0" x2="1" y2="1">
          <stop offset="0" stop-color="var(--band-green)"/>
          <stop offset="1" stop-color="var(--band-green-deep)"/>
        </linearGradient>
      </defs>
      <path class="lime-swoosh" fill="var(--lime)"
            d="M330,312 C520,300 700,380 800,400 C880,414 950,400 1000,384 L1000,432 C920,458 820,455 720,428 C600,396 480,330 330,312 Z"/>
      <path class="green-band" fill="url(#bandFill)"
            d="M0,360 C120,320 260,300 380,318 C520,340 620,420 760,446 C860,464 940,456 1000,444 L1000,571 L0,571 Z"/>
      <path class="white-rule" fill="none" stroke="#ffffff" stroke-width="4"
            d="M0,362 C120,322 260,302 380,320 C520,342 620,422 760,448 C860,466 940,458 1000,446"/>
    </svg>

    <div class="brand">
      <span class="brand-dot"></span>
      <span class="brand-name">Ferncrest Dental</span>
    </div>

    <p class="doctor-name">Dr. Lorna Pettigrew</p>

    <p class="contact contact-phone">ph: 610-555-0193</p>
    <p class="contact contact-email">ferncrestdental.office@examplemail.test</p>
    <p class="contact contact-address">2871 Marlowe Street<br>Bethlehem, PA 18093</p>
  </section>
</main>
</body>
</html>
```